Corporate Design für Büroservice
Zielgruppe
Wir bieten Dienstleistungen rund ums Büro wie z.b. Buchhaltung, Kommunikation ... für Unternehmen an.
Wir benötigen eine neue Website, da wir unser Unternehmen vergrößern und zusätzliche Dienstleitungen anbieten möchten.
Aufgabenstellung
Vorgaben haben wir keine nur sollte das Logo und der Rest zu unserer Branche passen und ansprechend wirken. Zudem sollte es Kompetenz und Seriosität vermitteln.
Visitenkarte und Briefbogen bitte mit den beigefügten Daten erstellen.

```html
<!DOCTYPE html>
<html lang="de">
<head>
<meta charset="utf-8">
<title>Hartwig Büroservice – Geschäftsausstattung</title>
<link href="https://fonts.googleapis.com/css2?family=Arimo:wght@400;700&display=swap" rel="stylesheet">
<style>
  :root {
    --teal: #00b5ad;
    --white: #ffffff;
    --page: #ffffff;
    --stage: #eeeeec;
    --ink: #666666;
    --ink-soft: #8a8a8a;
  }
  * { box-sizing: border-box; margin: 0; padding: 0; }
  html, body { width: 1200px; height: 2749px; overflow: hidden; background: var(--page); }
  body { position: relative; font-family: "Arimo", Arial, sans-serif; color: var(--ink); }

  .card, .letterhead, .stage {
    position: absolute;
    box-shadow: 0 6px 22px rgba(0,0,0,.16);
  }
  .card { width: 521px; height: 315px; overflow: hidden; }
  .card--teal { background: var(--teal); color: var(--white); }
  .card--white { background: var(--white); }

  .wordmark {
    font-family: "Arimo", Arial, sans-serif;
    font-weight: 700;
    color: var(--teal);
    letter-spacing: .5px;
    line-height: 1.05;
  }
  .card--teal .wordmark, .card--teal .contact { color: var(--white); }

  .front .wordmark {
    position: absolute; left: 0; right: 0; top: 50%;
    transform: translateY(-50%);
    text-align: center; font-size: 38px;
  }

  .back .side-band { position: absolute; left: 0; top: 0; bottom: 0; width: 28px; }
  .card--white.back .side-band { background: var(--teal); }
  .card--teal.back .side-band { background: var(--white); }
  .back .wordmark { position: absolute; left: 62px; top: 30px; font-size: 30px; }
  .contact {
    position: absolute; right: 17px; top: 126px;
    text-align: right; font-size: 15px; line-height: 18px; color: var(--ink-soft);
  }
  .contact .name { font-size: 23px; margin-bottom: 22px; color: var(--ink-soft); }
  .contact p + p { margin-top: 16px; }

  .letterhead { left: 91px; top: 841px; width: 1005px; height: 1383px; background: var(--white); }
  .letterhead .wordmark { position: absolute; left: 44px; top: 44px; font-size: 40px; }
  .sender-line {
    position: absolute; right: 91px; top: 274px; font-size: 18px; display: flex;
  }
  .sender-line span + span { border-left: 1.5px solid var(--ink); margin-left: 9px; padding-left: 9px; }
  .bank {
    position: absolute; right: 33px; top: 1147px; width: 320px;
    text-align: center; font-size: 20px; line-height: 23px;
  }
  .footer {
    position: absolute; left: 239px; top: 1293px; display: flex; font-size: 15px; line-height: 17px;
  }
  .footer div + div { border-left: 1.5px solid var(--ink); margin-left: 8px; padding-left: 8px; }
  .footer-band { position: absolute; left: 111px; width: 784px; bottom: 0; height: 31px; background: var(--teal); }

  .stage { width: 519px; height: 345px; background: var(--stage); box-shadow: none; }
  .stage .card { left: 50%; top: 50%; transform: translate(-50%, -50%) scale(.78); }
</style>
</head>
<body>

  <section class="card card--teal front" style="left:41px; top:25px;">
    <div class="wordmark">HARTWIG BÜROSERVICE</div>
  </section>

  <section class="card card--white back" style="left:625px; top:25px;">
    <div class="side-band"></div>
    <div class="wordmark">HARTWIG<br>BÜROSERVICE</div>
    <div class="contact">
      <div class="name">Lena Hartwig</div>
      <p>Lindenweg 14<br>88999 Wiesenfeld</p>
      <p>+4970001234567</p>
      <p>info@hartwig-bueroservice.de<br>www.hartwig-bueroservice.de</p>
    </div>
  </section>

  <section class="card card--white front" style="left:41px; top:386px;">
    <div class="wordmark">HARTWIG BÜROSERVICE</div>
  </section>

  <section class="card card--teal back" style="left:625px; top:386px;">
    <div class="side-band"></div>
    <div class="wordmark">HARTWIG<br>BÜROSERVICE</div>
    <div class="contact">
      <div class="name">Lena Hartwig</div>
      <p>Lindenweg 14<br>88999 Wiesenfeld</p>
      <p>+4970001234567</p>
      <p>info@hartwig-bueroservice.de<br>www.hartwig-bueroservice.de</p>
    </div>
  </section>

  <section class="letterhead">
    <div class="wordmark">HARTWIG<br>BÜROSERVICE</div>
    <div class="sender-line">
      <span>Lena Hartwig</span><span>Lindenweg 14</span><span>88999 Wiesenfeld</span>
    </div>
    <div class="bank">
      Bankverbindung<br>Musterbank Süd<br>IBAN:DE00100100100012345678<br>BIC:MUSTDE1SXXX
    </div>
    <div class="footer">
      <div>Lindenweg 14<br>88999 Wiesenfeld</div>
      <div>+4970001234567<br>UST.IDDE 000 111 222</div>
      <div>info@hartwig-bueroservice.de<br>www.hartwig-bueroservice.de</div>
    </div>
    <div class="footer-band"></div>
  </section>

  <section class="stage" style="left:51px; top:2319px;">
    <div class="card card--white front">
      <div class="wordmark">HARTWIG BÜROSERVICE</div>
    </div>
  </section>

  <section class="stage" style="left:622px; top:2319px;">
    <div class="card card--teal back">
      <div class="side-band"></div>
      <div class="wordmark">HARTWIG<br>BÜROSERVICE</div>
      <div class="contact">
        <div class="name">Lena Hartwig</div>
        <p>Lindenweg 14<br>88999 Wiesenfeld</p>
        <p>+4970001234567</p>
        <p>info@hartwig-bueroservice.de<br>www.hartwig-bueroservice.de</p>
      </div>
    </div>
  </section>

</body>
</html>
```